Korveth Signal Works DL Promo Flyer

This DL flyer is targeted at the corporate / business sector to promote our products and services to the professional market. Photos are worth a 1000 words hence they are intended to grasp initial interest. We would like the brochure to exceptionally high standard, reflect the high technology market we operate within yet be simple to understand. In the attached draft the text component is ideal but the layout and placement needs work, it needs an eye-catching front page. I would envisage a shaded image behind the texts and photos, the manufacturer logos could be shaded or remain as colour if not too distracting, just after a professional eye-catching design. have attached a draft and images that can be used, also need to fill in one panel with something and willing to discuss options there.

Target Market(s)

Corporate & Government sectors

Industry/Entity Type

Business

Font styles to use
Sans Serif

Colors
0355a3

Requirements
Must have
• Eye-catching, professional design and reflect the technology market we operate within. The brochure will be printed on high-gloss card opposed to paper to give it a professional appearance and hopefully assist in making it past the receptionist to the decision makers and purchasers. also Promote the fact we are a national company, Australian owned.
Nice to have
• Impressive photos - worth a thousand words - stunning front page that makes people want to open the brochure and know what it is.
Should not have
• Be cluttered and difficult to follow

```html
<!DOCTYPE html>
<html lang="en">
<head>
<meta charset="utf-8">
<title>Korveth Signal Works – DL Promo Flyer</title>
<link href="https://fonts.googleapis.com/css2?family=Hind:wght@300;400;500;600&family=Dosis:wght@500;600&display=swap" rel="stylesheet">
<style>
  :root{
    --canvas:#d8d9db;
    --blue:#4f8bbd;
    --blue-deep:#2f6ea6;
    --blue-light:#7fb0d8;
    --dark:#262628;
    --dark-2:#323235;
    --paper:#f2f2f3;
    --ink:#1d1d1f;
    --muted:#e8e9ea;
  }
  *{margin:0;padding:0;box-sizing:border-box}
  html,body{width:880px;height:1200px;overflow:hidden}
  body{background:var(--canvas);font-family:"Hind",Arial,sans-serif;color:var(--ink);position:relative}
  .spread{position:absolute;left:20px;width:840px;height:560px;display:flex;background:var(--paper);overflow:hidden}
  .spread--outside{top:30px}
  .spread--inside{top:610px}
  .panel{position:relative;width:280px;height:100%;overflow:hidden}
  .photo{position:absolute}
  .shape{position:absolute;inset:0;width:100%;height:100%}

  /* Outside – left panel */
  .panel--services{background:var(--blue)}
  .panel--services .photo{left:0;top:0;width:280px;height:360px;
    background:radial-gradient(circle at 40% 38%,#5fa9e6 0,#1b3c6a 30%,#0b1322 70%);
    clip-path:polygon(0 0,100% 0,100% 100%,0 58%)}
  .service{position:absolute;left:24px;width:228px;color:#fff}
  .service h3{font-weight:400;font-size:11px;letter-spacing:.2px;margin-bottom:4px}
  .service p{font-size:8px;line-height:9.5px;font-weight:400}
  .service--install{top:415px}
  .service--tech{top:480px}

  /* Outside – middle panel */
  .panel--intro{background:linear-gradient(90deg,#e4e5e6,#f7f7f7 60%,#eaeaeb)}
  .panel--intro .photo{left:40px;top:22px;width:200px;height:130px;border-radius:4px;
    background:linear-gradient(180deg,#1a1a1c,#2b5f92 40%,#1b3250 80%,#1a1a1c)}
  .intro-title{position:absolute;top:165px;width:100%;text-align:center;font-size:14px;font-weight:500;line-height:17px}
  .intro-title span{display:block;font-size:13px}
  .intro-body{position:absolute;top:210px;left:26px;width:228px;text-align:center;font-size:8px;line-height:12px}
  .intro-body strong{display:block;font-weight:600}
  .contact{position:absolute;right:18px;top:440px;text-align:right;color:var(--blue-light);font-family:"Dosis",sans-serif;letter-spacing:.6px}
  .contact .join{font-size:17px;font-weight:600;color:var(--blue)}
  .contact div{font-size:10.5px;line-height:17px}
  .contact .phone{font-size:13px;display:flex;align-items:center;justify-content:flex-end;gap:4px}

  /* Outside – right panel */
  .panel--cover{background:var(--dark)}
  .panel--cover .photo{left:0;top:0;width:280px;height:360px;
    background:linear-gradient(180deg,#8fa7c0,#c9ccd0 45%,#e8e6e2);
    clip-path:polygon(0 0,100% 0,100% 100%,0 100%)}
  .brand{position:absolute;left:20px;top:493px;display:flex;align-items:center;gap:10px;color:#fff}
  .brand-square{width:26px;height:26px;background:var(--blue)}
  .brand-name{font-size:16px;font-weight:500;line-height:17px}
  .brand-tag{font-size:8.5px;font-weight:400;color:#ececec}

  /* Inside – left panel */
  .panel--about{background:#fff}
  .about-head{position:absolute;top:148px;left:24px;display:flex;align-items:center;gap:10px}
  .about-head i{display:block;width:18px;height:18px;background:var(--blue-deep)}
  .about-head h2{font-size:17px;font-weight:400;color:var(--blue);letter-spacing:.3px}
  .about-body{position:absolute;top:200px;left:22px;width:238px;font-size:8.4px;line-height:10.6px;text-align:justify}
  .about-body p{margin-bottom:10px}

  /* Inside – product panels */
  .panel--products{background:linear-gradient(90deg,#e9eaeb,#f7f7f7 50%,#eeeeef)}
  .product{position:absolute;left:8px;width:268px;height:104px}
  .product h4{font-size:8.6px;font-weight:400;letter-spacing:.3px;line-height:10px}
  .product .photo{left:0;top:11px;width:108px;height:80px}
  .product p{position:absolute;left:112px;top:8px;width:150px;font-size:7.3px;line-height:9px}
  .p1{top:8px}.p2{top:112px}.p3{top:216px}.p4{top:320px}.p5{top:424px}
  .tone-warm{background:linear-gradient(160deg,#6b5a44,#b79a6e 60%,#3a3028)}
  .tone-cool{background:linear-gradient(160deg,#cfd6da,#8a949a 60%,#4e5659)}
  .tone-blue{background:linear-gradient(160deg,#1f2d4a,#3e6fa8 55%,#141b2a)}
  .tone-hall{background:linear-gradient(180deg,#b7aa8e,#5b5d78 55%,#2e2f44)}
  .tone-gym{background:linear-gradient(160deg,#2a2d31,#6f747a 55%,#1a1b1d)}
  .tone-device{background:linear-gradient(180deg,#111,#2f6ea6 45%,#1d3350 85%,#111)}

  /* Partner strip */
  .partners{position:absolute;left:20px;top:1138px;width:840px;height:32px;background:#e9eaeb;
    display:flex;align-items:center;justify-content:space-around;padding:0 10px;
    font-size:11px;font-weight:600;color:#3a3a3d;letter-spacing:.3px}
</style>
</head>
<body>

<!-- OUTSIDE SPREAD -->
<section class="spread spread--outside">
  <article class="panel panel--services">
    <div class="photo" role="img" aria-label="Glowing curved strip of technology photos wrapping around a globe"></div>
    <svg class="shape" viewBox="0 0 280 560" aria-hidden="true">
      <polygon points="0,209 280,360 280,0 230,0" fill="#3b76a8" opacity=".55"/>
      <polygon points="0,560 280,560 280,430" fill="#3f78aa" opacity=".5"/>
    </svg>
    <div class="service service--install">
      <h3>› AV INSTALLATIONS</h3>
      <p>With our highly skilled team of AV technicians we can also perform your custom installation to a professional standard</p>
    </div>
    <div class="service service--tech">
      <h3>› SERVICE TECHNICIANS</h3>
      <p>Korveth Signal Works offer a complete after-sales support service for all types of audio visual products including repairs, parts, and on-site service</p>
    </div>
  </article>

  <article class="panel panel--intro">
    <svg class="shape" viewBox="0 0 280 560" aria-hidden="true">
      <polygon points="0,300 0,560 280,560 280,330 140,430" fill="var(--dark)"/>
      <polygon points="0,300 100,490 0,560" fill="var(--blue)"/>
      <polygon points="0,300 100,490 150,420" fill="#6a9cc6"/>
    </svg>
    <div class="photo" role="img" aria-label="Wall-mounted touch control panel showing a media player screen"></div>
    <h1 class="intro-title">MAKING A DIFFERENCE<span>in a Changing World</span></h1>
    <div class="intro-body">
      <strong>Korveth Signal Works</strong>
      was established in Melbourne in June of 2000. With offices in Melbourne, Sydney, Brisbane and Perth we provide state based, national and global organisations a complete, consistent and diverse range of audio visual products and services.
    </div>
    <div class="contact">
      <div class="join">JOIN US</div>
      <div>info@korvethsignal.com.au</div>
      <div class="phone"><svg width="11" height="11" viewBox="0 0 24 24"><path fill="currentColor" d="M6.6 10.8a15 15 0 0 0 6.6 6.6l2.2-2.2c.3-.3.7-.4 1-.2 1.1.4 2.3.6 3.6.6.6 0 1 .4 1 1V20c0 .6-.4 1-1 1A17 17 0 0 1 3 4c0-.6.4-1 1-1h3.5c.6 0 1 .4 1 1 0 1.3.2 2.5.6 3.6.1.3 0 .7-.2 1z"/></svg>1300 555 017</div>
      <div>MELBOURNE-SYDNEY-BRISBANE-PERTH</div>
      <div>www.korvethsignal.com.au</div>
    </div>
  </article>

  <article class="panel panel--cover">
    <div class="photo" role="img" aria-label="Airport terminal concourse with large video wall and departure screens"></div>
    <svg class="shape" viewBox="0 0 280 560" aria-hidden="true">
      <polygon points="0,340 140,430 280,330 280,560 0,560" fill="var(--dark)"/>
    </svg>
    <div class="brand">
      <span class="brand-square"></span>
      <div>
        <div class="brand-name">Korveth Signal Works</div>
        <div class="brand-tag">Connecting people with technology</div>
      </div>
    </div>
  </article>
</section>

<!-- INSIDE SPREAD -->
<section class="spread spread--inside">
  <article class="panel panel--about">
    <svg class="shape" viewBox="0 0 280 560" aria-hidden="true">
      <polygon points="0,0 280,0 280,70 120,140 0,30" fill="#ececed"/>
      <polygon points="0,0 150,0 60,80" fill="var(--blue)"/>
      <polygon points="0,0 0,30 60,80" fill="#3b76a8"/>
      <polygon points="0,500 280,470 280,560 0,560" fill="var(--blue)"/>
    </svg>
    <div class="about-head"><i></i><h2>WHO ARE WE?</h2></div>
    <div class="about-body">
      <p>Korveth Signal Works are a dedicated team of Audio Visual professionals whose extensive industry experience, customer focus and purchasing power result in outstanding presentation solutions designed to make you look GREAT!</p>
      <p>We offer state-of-the-art technology combined with reliability, professional service and value for money to our customers. With offices located in Melbourne, Sydney, Brisbane and Perth we are well positioned to provide national coverage for business both small and large.</p>
      <p>We don’t just sell products, anyone can do that, we specialise in asking the questions in order to understand your unique needs, offer our advice and then design strategic options to meet your needs to deliver the optimum communications environment.</p>
      <p>With our expert guidance, industry knowledge, guidance and patience, Korveth Signal Works will offer you a user-friendly, customised solution at the best value to meet your needs.</p>
    </div>
  </article>

  <article class="panel panel--products">
    <div class="product p1"><h4>BOARDROOMS</h4>
      <div class="photo tone-warm" role="img" aria-label="Boardroom with long table and presentation screen"></div>
      <p>Impress your clients using the latest technology and professional AV equipment so you can concentrate on your presentation and them with total confidence in your equipment.</p></div>
    <div class="product p2"><h4>MEETING ROOMS</h4>
      <div class="photo tone-cool" role="img" aria-label="Bright meeting room with table and chairs"></div>
      <p>Many meeting rooms are now multi-purpose and need to cater for a variety of uses – we can ensure you have the right equipment to maximise upon these spaces.</p></div>
    <div class="product p3"><h4>VIDEO CONFERENCING</h4>
      <div class="photo tone-cool" role="img" aria-label="Video conference room with remote participants on screen"></div>
      <p>Experience why so many organisations have embraced collaboration. From Chatterline, Meetwave, JoinHub right through to high-end video conferencing platforms. We will guide you every step of the way.</p></div>
    <div class="product p4"><h4>LARGE VENUES</h4>
      <div class="photo tone-hall" role="img" aria-label="Tiered lecture theatre with projection screen"></div>
      <p>Large-venue spaces require speciality integration skills to ensure delivery of effectiveness in both video and audio equipment with ease-of-use a paramount requirement.</p></div>
    <div class="product p5"><h4>SPORT &amp; RECREATION</h4>
      <div class="photo tone-gym" role="img" aria-label="Gym with treadmills and wall-mounted screens"></div>
      <p>One of the fastest growing markets in Australia, Korveth Signal Works have been providing design, installation and technical services to this exciting sector for over 15 years.</p></div>
  </article>

  <article class="panel panel--products">
    <svg class="shape" viewBox="0 0 280 560" aria-hidden="true">
      <polygon points="200,0 280,0 280,60" fill="var(--blue)"/>
    </svg>
    <div class="product p1"><h4>PROJECTORS</h4>
      <div class="photo tone-warm" role="img" aria-label="Projector on a desk beaming light"></div>
      <p>Projectors remain a popular and effective presentation tool and the technology and options available today is astounding. Let us help decide what is right for you from a range of manufacturers.</p></div>
    <div class="product p2"><h4>LED TOUCHSCREENS</h4>
      <div class="photo tone-blue" role="img" aria-label="Large interactive touchscreen display in use"></div>
      <p>Our extensive experience in the area of interactive touchscreens is second-to-none. This impressive technology is ideal for meeting rooms, collaboration, brain-storming, training rooms and more. Ask us for a free demonstration.</p></div>
    <div class="product p3"><h4>VIDEO WALLS</h4>
      <div class="photo tone-blue" role="img" aria-label="Multi-screen video wall in a dark room"></div>
      <p>Larger and more impressive screens are required in many applications now and with multi-screen video wall sizes virtually unlimited the image quality is stunning. A very cost effective solution for high quality large images.</p></div>
    <div class="product p4"><h4>DIGITAL SIGNAGE</h4>
      <div class="photo tone-warm" role="img" aria-label="Digital signage screen in a lobby"></div>
      <p>What better way to get your message around the organisation than digital signage. All managed using a web-browser and suitable from one screen to thousands all on the same network!</p></div>
    <div class="product p5"><h4>AV CONTROL SYSTEMS</h4>
      <div class="photo tone-device" role="img" aria-label="Touch control panel for an AV system"></div>
      <p>Do you have the one person you reply upon to set up and get your AV equipment operational – you might need to consider a user-friendly control system to start, control and switch off everything from your finger-tips.</p></div>
  </article>
</section>

<div class="partners">
  <span>Norvik</span><span>Calloway</span><span>Tresk</span><span>Ventrolux</span><span>Arbenza</span><span>Quilmar</span><span>Dellfor</span><span>Orrivane</span><span>Pelt</span><span>Zorrel</span><span>Havrin</span><span>Mostrel</span><span>Kenlo</span>
</div>

</body>
</html>
```